Brightmoor Partners Branding Revamp

We are a consulting company, looking for a way to display and promote our brand. We have 2 sides to the business- Brightmoor (financial) and Partners (cyber security). The financial side products relate to business necessities: card processing, website design/hosting/maintenance, VoIP phone systems. The cyber security side promotes a bundled package of 4 solutions: network vulnerability scan, dark web scan, anti-ransomeware/malware software, and image-level backups. We want people to understand that partnering with Brightmoor Partners gives them “Elevated Peace of Mind” (tagline). Current badge and logos uploaded.

Target Market(s)

Small businesses

Contact Information for Business Card

Lena Marwick, Vice President, lena@brightmoorpartners.example, 555-806-1937, www.brightmoorpartners.example

Requirements
Nice to have
• I do prefer the darker background for front and back

```html
<!DOCTYPE html>
<html lang="en">
<head>
<meta charset="utf-8">
<title>Brightmoor Partners — Business Card</title>
<link rel="stylesheet" href="https://fonts.googleapis.com/css2?family=Montserrat:wght@400;500;600;700&display=swap">
<style>
  :root {
    --backdrop: #b6b6b6;
    --card-dark: #333132;
    --card-light: #e1e0e4;
    --brand-red: #d9141b;
    --ink-white: #ffffff;
    --ink-soft: #d8d8d8;
    --ink-grey: #555459;
    --ink-dark: #3e3d42;
    --rule: #8f8e93;
  }
  * { margin: 0; padding: 0; box-sizing: border-box; }
  html, body {
    width: 1200px; height: 900px; overflow: hidden;
    background: var(--backdrop);
    font-family: "Montserrat", Arial, sans-serif;
  }
  .card {
    position: absolute;
    left: 363px;
    width: 475px; height: 271px;
  }
  .card--front { top: 145px; background: var(--card-dark); }
  .card--back { top: 484px; background: var(--card-light); }

  /* Front */
  .front-mark {
    position: absolute; left: 50%; top: 84px;
    width: 28px; height: 28px; margin-left: -14px;
    background: var(--brand-red);
  }
  .front-wordmark {
    position: absolute; left: 0; right: 0; top: 140px;
    text-align: center;
    color: var(--ink-white);
    font-weight: 600; font-size: 19px; line-height: 24px;
    letter-spacing: 0.28em;
    text-transform: uppercase;
    padding-left: 0.28em;
  }
  .tagline {
    position: absolute; left: 0; right: 0; top: 222px;
    text-align: center;
    color: var(--ink-soft);
    font-size: 10.5px; font-weight: 500;
    letter-spacing: 0.26em;
    padding-left: 0.26em;
  }

  /* Back */
  .back-mark {
    position: absolute; left: 49px; top: 52px;
    width: 22px; height: 22px;
    background: var(--brand-red);
  }
  .back-wordmark {
    position: absolute; left: 49px; top: 88px;
    color: var(--ink-dark);
    font-weight: 600; font-size: 13px;
    letter-spacing: 0.22em;
    text-transform: uppercase;
  }
  .person-name {
    position: absolute; right: 48px; top: 136px;
    color: var(--brand-red);
    font-weight: 700; font-size: 14.5px; line-height: 18px;
    text-transform: uppercase;
  }
  .title-row {
    position: absolute; left: 49px; right: 48px; top: 155px;
    display: flex; align-items: center;
  }
  .divider {
    flex: 1; height: 1px; margin-right: 5px;
    background: var(--rule);
  }
  .person-title {
    color: var(--ink-grey);
    font-size: 11px; line-height: 14px;
    white-space: nowrap;
  }
  .service-list {
    position: absolute; left: 49px; top: 182px;
    list-style: none;
    color: var(--ink-grey);
    font-size: 10.5px; line-height: 13.6px;
    white-space: nowrap;
  }
  .service-list li { display: flex; align-items: center; }
  .service-list li::before {
    content: ""; width: 6px; height: 6px; margin-right: 8px;
    background: var(--brand-red);
  }
  .contact-list {
    position: absolute; right: 48px; top: 195.6px;
    list-style: none;
    color: var(--ink-grey);
    font-size: 9.5px; line-height: 13.6px;
    text-align: right;
    white-space: nowrap;
  }
  .contact-list li { display: flex; justify-content: flex-end; align-items: center; }
  .contact-list svg { width: 9px; height: 9px; margin-left: 6px; flex: none; }
</style>
</head>
<body>
  <section class="card card--front">
    <div class="front-mark"></div>
    <h1 class="front-wordmark">Brightmoor Partners</h1>
    <p class="tagline">ELEVATED PEACE OF MIND</p>
  </section>

  <section class="card card--back">
    <div class="back-mark"></div>
    <div class="back-wordmark">Brightmoor Partners</div>

    <h2 class="person-name">Lena Marwick</h2>
    <div class="title-row">
      <div class="divider"></div>
      <p class="person-title">Vice President</p>
    </div>

    <ul class="service-list">
      <li>Credit Card Processing</li>
      <li>Digital Phone Service</li>
      <li>Business Internet</li>
      <li>Business Email, CloudDesk 365</li>
    </ul>

    <ul class="contact-list">
      <li>555-806-1937
        <svg viewBox="0 0 10 10" aria-hidden="true"><path d="M2 1 L4 1 L4.6 3 L3.5 3.8 Q4.5 5.8 6.2 6.5 L7 5.4 L9 6 L9 8 Q5 9 2.2 6 Q0.6 3.5 2 1 Z" fill="var(--brand-red)"/></svg>
      </li>
      <li>lena@brightmoorpartners.example
        <svg viewBox="0 0 10 10" aria-hidden="true"><rect x="0.5" y="2" width="9" height="6" fill="var(--brand-red)"/><path d="M0.5 2 L5 5.5 L9.5 2" stroke="var(--card-light)" stroke-width="0.9" fill="none"/></svg>
      </li>
      <li>www.brightmoorpartners.example
        <svg viewBox="0 0 10 10" aria-hidden="true"><g fill="none" stroke="var(--brand-red)" stroke-width="0.9"><circle cx="5" cy="5" r="4.2"/><ellipse cx="5" cy="5" rx="1.8" ry="4.2"/><path d="M0.8 5 H9.2 M1.6 3 H8.4 M1.6 7 H8.4"/></g></svg>
      </li>
    </ul>
  </section>
</body>
</html>
```